依頼詳細
犬と一緒にアウトドアを楽しめる商品の企画・製造・販売を手掛けます。
先日当サイトで募集したロゴが確定しましたので、そちらを用いた名刺のデザイン案をお寄せください。名刺は2、3色以内で活版印刷を予定しています(単色も可)ので、グラデーションなどを使用しないデザインをお願いいたします。
記載項目
以下の項目が含まれていれば、レイアウトなども含め特に制限はありません。
表面は「屋号」「役職」「氏名」「氏名ローマ字」「郵便番号」「所在地1」「所在地2」「電話番号」「メールアドレス」「URL」
裏面は「ロゴ」キャラだけ文字だけでも可
希望イメージ
シンプル 複雑
単色 カラフル
暗い 明るい
日常 高級
遊び心 厳粛
未来的 伝統的
女性的 男性的
希望する色
納品ファイル
• 高解像度JPG (.jpg)
• イラストレーター形式 (.ai)
• PNG形式 (.png)
補足説明
ブランド名
PIREL(ぴれる)※屋号ではない
所在地について
「所在地1:都道府県市区町村番地」「所在地2:建物名フロア」となります。
例)
〒1234567
所在地1県所在地1市所在地1区所在地1-2-3
所在地2ビル所在地2階

活版印刷での名刺を想定しておりましたので割とシンプルなデザインの提案が多い中、
ブランド特性に配慮いただき遊び心を取り入れていただいたところがポイントと
なりました。

事業が動き出したばかりということもあり、今後もご協力をいただく機会があるかと
思いますので、その節はまた提案いただけると助かります。

```html
<!DOCTYPE html>
<html lang="ja">
<head>
<meta charset="utf-8">
<title>PIREL 名刺</title>
<link rel="stylesheet" href="https://fonts.googleapis.com/css2?family=Didact+Gothic&family=Noto+Sans+JP:wght@400;500&display=swap">
<style>
  :root {
    --paper: #ffffff;
    --ink: #222222;
    --brand-green: #9ccf9c;
    --on-green: #ffffff;
  }
  html, body {
    margin: 0;
    padding: 0;
    width: 725px;
    height: 1200px;
    overflow: hidden;
    background: var(--paper);
  }
  .card {
    position: relative;
    width: 725px;
    height: 1200px;
    background: var(--paper);
    color: var(--ink);
    font-family: "Didact Gothic", "Noto Sans JP", sans-serif;
    overflow: hidden;
  }
  .corner-band {
    position: absolute;
    inset: 0;
    width: 725px;
    height: 1200px;
  }
  .corner-band polygon { fill: var(--brand-green); }
  .brand-mark {
    position: absolute;
    top: 198px;
    left: 470px;
    width: 200px;
    text-align: center;
    color: var(--on-green);
    font-family: "Didact Gothic", sans-serif;
    font-size: 50px;
    letter-spacing: 0.04em;
    line-height: 1;
  }
  .line {
    position: absolute;
    left: 73px;
    margin: 0;
    white-space: nowrap;
    line-height: 1;
  }
  .title {
    top: 466px;
    font-family: "Noto Sans JP", sans-serif;
    font-size: 31px;
  }
  .name {
    top: 540px;
    font-family: "Noto Sans JP", sans-serif;
    font-weight: 500;
    font-size: 54px;
    letter-spacing: 1.02em;
  }
  .name-roman {
    top: 614px;
    font-size: 33px;
    letter-spacing: 0.4em;
  }
  .contact { font-size: 37px; letter-spacing: 0.05em; }
  .phone { top: 740px; }
  .email { top: 798px; }
  .url { top: 854px; }
  .address { font-family: "Noto Sans JP", "Didact Gothic", sans-serif; font-size: 35px; letter-spacing: 0.02em; }
  .trade-name { top: 968px; }
  .postal { top: 1026px; font-family: "Didact Gothic", sans-serif; font-size: 37px; letter-spacing: 0.05em; }
  .street { top: 1078px; }
</style>
</head>
<body>
  <div class="card">
    <svg class="corner-band" viewBox="0 0 725 1200" aria-hidden="true">
      <polygon points="278,0 725,0 725,722"/>
    </svg>

    <div class="brand-mark">PIREL</div>

    <p class="line title">代表取締役社長</p>
    <p class="line name">比蓮一郎</p>
    <p class="line name-roman">Pirel Ichiro</p>

    <p class="line contact phone">0120-987-6543</p>
    <p class="line contact email">pirel.ichiro@pirel.com</p>
    <p class="line contact url">https://pirel.com</p>

    <p class="line address trade-name">○○屋号○○</p>
    <p class="line address postal">765-4321</p>
    <p class="line address street">東京都○○市○○区○2-18</p>
  </div>
</body>
</html>
```